Logo, banner, business card & stationary for "Harbor Capital"

Harbor Capital

I need logo graphic with text, banner, A4 stationary & business card

Key Words for the Logo
======================
Trustworthy
Successful
Safe
Loyal
Eye catching
Attractive
Elegant
High class
Easily recognisable outline
Looks good on a fax. Ie in B&W

Notes
=====
Stationary: A4
Illustrator CS3
Full Color
Standard W10 Fonts [if use others, you must give them to me]
Do NOT flatten the fonts
Layers & Objects must be organised nicely, because I need to translate the English into Chinese.
Vector graphic only

Contact details for the stationary:
Harbor Capital
Gerald T. Finch
47, Lishan Rd, Fengyuan, Taichung
0952 418 418 <--- my cell. Make this bigger/clearer
(04) 2736 4821
service@harborcap.com
harbor5273.com

Please add the "Chatto" QR code to the card and stationary

Target Market(s)

Rich people with money looking for a *safe* investment.

Industry/Entity Type

Investment

Font styles to use
Sans Serif

Requirements
Must have
• Safe, reliable
Nice to have
• Please look at the tower & comet logos below.
• Tower - strong, building up
• Comet - shiny/bright and great success
• Could our logo have these 2 elements
Should not have
• Too modern

```html
<!DOCTYPE html>
<html lang="en">
<head>
<meta charset="utf-8">
<title>Harbor Capital – Business Card</title>
<link rel="stylesheet" href="https://fonts.googleapis.com/css2?family=PT+Sans:wght@400;700&display=swap">
<style>
  :root {
    --ink: #1e1e1e;
    --sky: #78b6d0;
    --paper: #ffffff;
    --sans: "PT Sans", Arial, sans-serif;
  }
  html, body {
    margin: 0;
    padding: 0;
    width: 1200px;
    height: 650px;
    overflow: hidden;
    background: var(--paper);
  }
  .card {
    position: relative;
    width: 1200px;
    height: 650px;
    background: var(--paper);
    font-family: var(--sans);
    color: var(--paper);
  }
  .card-front {
    position: absolute;
    left: 0;
    top: 0;
    width: 601px;
    height: 650px;
    background: var(--ink);
  }
  .brand {
    position: absolute;
    left: 0;
    top: 226px;
    width: 601px;
    text-align: center;
  }
  .brand-mark {
    display: block;
    margin: 0 auto 26px;
  }
  .brand-name {
    margin: 0;
    font-weight: 400;
    line-height: 1.08;
    color: var(--paper);
    letter-spacing: 0.02em;
  }
  .brand-name .line-one { display: block; font-size: 74px; }
  .brand-name .line-two { display: block; font-size: 56px; }
  .address {
    position: absolute;
    left: 0;
    width: 601px;
    top: 578px;
    margin: 0;
    text-align: center;
    font-size: 24px;
    font-style: normal;
  }
  .card-back {
    position: absolute;
    left: 622px;
    top: 2px;
    width: 578px;
    height: 646px;
    background: var(--sky);
  }
  .person {
    position: absolute;
    right: 57px;
    top: 258px;
    margin: 0;
    font-size: 70px;
    font-weight: 400;
    line-height: 1;
  }
  .contact {
    position: absolute;
    right: 57px;
    top: 380px;
    margin: 0;
    padding: 0;
    list-style: none;
    text-align: right;
    font-size: 35px;
    line-height: 49px;
  }
  .contact .cell {
    font-size: 42px;
    font-weight: 700;
  }
</style>
</head>
<body>
  <div class="card">
    <section class="card-front">
      <div class="brand">
        <svg class="brand-mark" width="76" height="76" viewBox="0 0 76 76" aria-hidden="true">
          <circle cx="38" cy="38" r="36" fill="var(--sky)"/>
        </svg>
        <h1 class="brand-name">
          <span class="line-one">HARBOR</span>
          <span class="line-two">CAPITAL</span>
        </h1>
      </div>
      <address class="address">47 Lishan Rd / Fengyuan / Taichung</address>
    </section>
    <section class="card-back">
      <h2 class="person">Gerald T. Finch</h2>
      <ul class="contact">
        <li class="cell">Cell: 0952 418 418</li>
        <li>Tel: (04) 2736 4821</li>
        <li>Email: service@harborcap.com</li>
        <li>Website: harbor5273.com</li>
      </ul>
    </section>
  </div>
</body>
</html>
```